I need a design to display a result on a range line

For example - If I have a blood sugar result and I want to display it on a line so that I can display it in picture terms so that it can be understood more.
I want to input the result in a calculator so it can be displayed on the range line.

I want it so I can customise it and apply it to other results my self too.

```html
<!DOCTYPE html>
<html lang="en">
<head>
<meta charset="utf-8">
<title>Blood Sugar Range Line</title>
<link rel="stylesheet" href="https://fonts.googleapis.com/css2?family=Carlito:wght@400;700&display=swap">
<style>
  :root {
    --canvas-bg: #ffffff;
    --text: #111111;
    --axis: #7f7f7f;
    --low: #0078ff;
    --optimal: #00c853;
    --prediabetic: #ffc10a;
    --high: #ff5722;
    --very-high: #990000;
    --optimal-panel: #eaf7f1;
    --high-panel: #f7eaea;
  }
  html, body {
    margin: 0;
    padding: 0;
    overflow: hidden;
    background: var(--canvas-bg);
  }
  .canvas {
    position: relative;
    width: 1200px;
    height: 675px;
    overflow: hidden;
    background: var(--canvas-bg);
    font-family: "Carlito", "Calibri", sans-serif;
    color: var(--text);
  }
  .highlight {
    position: absolute;
    top: 211px;
    width: 176px;
    height: 198px;
    border-radius: 26px;
  }
  .highlight--optimal { left: 319px; background: var(--optimal-panel); }
  .highlight--high { left: 708px; background: var(--high-panel); }
  .range-axis {
    position: absolute;
    left: 0;
    top: 0;
    width: 1200px;
    height: 675px;
  }
  .range-stop {
    position: absolute;
    top: 237px;
    width: 160px;
    margin-left: -80px;
    text-align: center;
    font-weight: 700;
    font-size: 20px;
    line-height: 20px;
    white-space: nowrap;
  }
  .range-stop__value { display: block; height: 20px; }
  .range-stop__label { display: block; margin-top: 113px; }
</style>
</head>
<body>
  <main class="canvas">
    <div class="highlight highlight--optimal"></div>
    <div class="highlight highlight--high"></div>

    <svg class="range-axis" viewBox="0 0 1200 675" aria-hidden="true">
      <line x1="211" y1="309.5" x2="977" y2="309.5" stroke="var(--axis)" stroke-width="1.5"/>
      <circle cx="211" cy="309.5" r="34" fill="var(--low)"/>
      <circle cx="407" cy="309.5" r="34" fill="var(--optimal)"/>
      <circle cx="604" cy="309.5" r="34" fill="var(--prediabetic)"/>
      <circle cx="801" cy="309.5" r="34" fill="var(--high)"/>
      <circle cx="977" cy="309.5" r="34" fill="var(--very-high)"/>
    </svg>

    <div class="range-stop" style="left:211px">
      <span class="range-stop__value">&lt;4.0</span>
      <span class="range-stop__label">Low</span>
    </div>
    <div class="range-stop" style="left:408px">
      <span class="range-stop__value">4.0-5.59</span>
      <span class="range-stop__label">Optimal</span>
    </div>
    <div class="range-stop" style="left:596px">
      <span class="range-stop__value">5.6-6.99</span>
      <span class="range-stop__label">Pre-Diabetic</span>
    </div>
    <div class="range-stop" style="left:796px">
      <span class="range-stop__value">&ge;7.0</span>
      <span class="range-stop__label">High</span>
    </div>
    <div class="range-stop" style="left:977px">
      <span class="range-stop__value" style="margin-left:-10px">&ge;7.0</span>
      <span class="range-stop__label" style="margin-left:4px">Very High</span>
    </div>
  </main>
</body>
</html>
```